Electrical company business card design.

Hi, were an electrical company in Harbourton New Zealand called Quarneth Ltd. We focus mainly on high end residential and commercial so the card would be targeted towards that.
The card will be for myself, i am the director of the company.
Name: Derek Olstow
Position: Director/electrician
Phone: 021 387 9415
Email: derek@quarneth.co.nz
Location: Harbourton
As for colors the the blue color in the logo is preferred, i also don't mind a black background option.
Target Market(s)
High end residential and commercial
Industry/Entity Type
Electrician
Contact Information for Business Card
Name: Derek Olstow Position: Director/Electrician Phone: 021 387 9415, Email: derek@quarneth.co.nz, Location: Harbourton

```html
<!DOCTYPE html>
<html lang="en">
<head>
<meta charset="utf-8">
<title>Quarneth Ltd – Business Card</title>
<link rel="stylesheet" href="https://fonts.googleapis.com/css2?family=Open+Sans:wght@400;600;700;800&display=swap">
<style>
  :root {
    --backdrop: #a7a8ac;
    --card-white: #ffffff;
    --card-black: #000000;
    --ink-grey: #6d6e71;
    --ink-dark: #414042;
    --blue-light: #1a9ad8;
    --blue-deep: #0b55a6;
    --rule: #b9babd;
  }
  * { margin: 0; padding: 0; box-sizing: border-box; }
  html, body { width: 1025px; height: 1200px; overflow: hidden; }
  body {
    background: var(--backdrop);
    font-family: "Open Sans", Arial, sans-serif;
    position: relative;
  }
  .card {
    position: absolute;
    left: 155px;
    width: 715px;
    height: 431px;
    box-shadow: 9px 9px 10px rgba(0,0,0,0.45);
    overflow: hidden;
  }
  .card--front { top: 156px; background: var(--card-white); }
  .card--back { top: 628px; background: var(--card-black); }

  .brand {
    position: absolute;
    display: flex;
    flex-direction: column;
  }
  .brand__row { display: flex; align-items: center; gap: 10px; }
  .brand__dot {
    width: 26px; height: 26px; border-radius: 50%;
    background: var(--blue-light);
  }
  .brand__name {
    font-weight: 800;
    font-size: 42px;
    line-height: 1;
    letter-spacing: 1px;
    text-transform: uppercase;
  }
  .brand__tagline {
    font-weight: 700;
    font-size: 12.5px;
    letter-spacing: 0.6px;
    margin-top: 6px;
    margin-left: 36px;
    text-transform: uppercase;
  }
  .card--front .brand { left: 58px; top: 172px; }
  .card--front .brand__name,
  .card--front .brand__tagline { color: var(--ink-dark); }

  .card--back .brand { left: 50%; top: 50%; transform: translate(-50%, -50%); }
  .card--back .brand__name,
  .card--back .brand__tagline { color: var(--card-white); }
  .card--back .brand__dot { background: var(--card-white); }

  .divider {
    position: absolute;
    left: 390px; top: 96px;
    width: 1px; height: 241px;
    background: var(--rule);
  }
  .contact { position: absolute; left: 425px; top: 140px; color: var(--ink-grey); }
  .contact__name { font-size: 29px; font-weight: 600; line-height: 1.1; }
  .contact__role { font-size: 18px; margin-top: 6px; }
  .contact__list { list-style: none; margin-top: 22px; }
  .contact__item {
    display: flex; align-items: center; gap: 9px;
    font-size: 15.5px; margin-bottom: 12px;
  }
  .contact__icon { width: 15px; height: 15px; flex: none; }

  .band { position: absolute; left: 0; top: 0; width: 715px; height: 431px; }
</style>
</head>
<body>
  <section class="card card--front" aria-label="Business card front">
    <svg class="band" viewBox="0 0 715 431" aria-hidden="true">
      <defs>
        <linearGradient id="bandBlue" x1="0" y1="0" x2="1" y2="1">
          <stop offset="0" stop-color="#1a9ad8"/>
          <stop offset="0.6" stop-color="#1487cf"/>
          <stop offset="1" stop-color="#0b55a6"/>
        </linearGradient>
      </defs>
      <polygon points="0,431 540,360 472,341 715,291 715,431" fill="url(#bandBlue)"/>
    </svg>

    <div class="brand">
      <div class="brand__row">
        <span class="brand__dot"></span>
        <span class="brand__name">Quarneth</span>
      </div>
      <span class="brand__tagline">Wired for excellence</span>
    </div>

    <div class="divider"></div>

    <div class="contact">
      <p class="contact__name">Derek Olstow</p>
      <p class="contact__role">Director/electrician</p>
      <ul class="contact__list">
        <li class="contact__item">
          <svg class="contact__icon" viewBox="0 0 16 16" aria-hidden="true">
            <circle cx="8" cy="8" r="8" fill="#6d6e71"/>
            <path d="M5.2 4.2l1.4-.3.8 1.9-1 .7c.5 1.1 1.3 1.9 2.3 2.4l.7-1 1.9.8-.3 1.4c-3.2.3-6.1-2.6-5.8-5.9z" fill="#fff"/>
          </svg>
          <span>021 387 9415</span>
        </li>
        <li class="contact__item">
          <svg class="contact__icon" viewBox="0 0 16 16" aria-hidden="true">
            <path d="M8 0.5a5.5 5.5 0 0 0-5.5 5.5c0 4 5.5 9.5 5.5 9.5s5.5-5.5 5.5-9.5A5.5 5.5 0 0 0 8 0.5z" fill="#6d6e71"/>
            <circle cx="8" cy="6" r="2.2" fill="#fff"/>
          </svg>
          <span>Harbourton</span>
        </li>
      </ul>
    </div>
  </section>

  <section class="card card--back" aria-label="Business card back">
    <div class="brand">
      <div class="brand__row">
        <span class="brand__dot"></span>
        <span class="brand__name">Quarneth</span>
      </div>
      <span class="brand__tagline">Wired for excellence</span>
    </div>
  </section>
</body>
</html>
```